Bar and Grill needs specials signage

I have attached a file called "daily specials" I need it changed - so there is 1 sign/poster for each day/special
also attached other items to show some styling. I want the new posters chalkboard format, styled along the lines of the drink designs attached.
The designs should be scaleable, and editable, I will print locally

```html
<!DOCTYPE html>
<html lang="en">
<head>
<meta charset="utf-8">
<title>Daily Special – Friday</title>
<link rel="stylesheet" href="https://fonts.googleapis.com/css2?family=Rye&family=Bangers&display=swap">
<style>
  :root {
    --board-dark: #0b0d10;
    --board-mid: #2a2e33;
    --board-light: #3c4147;
    --frame-line: #9aa3ab;
    --frame-blue: #2b8fb8;
    --bolt-blue: #3a9cc4;
    --chalk-white: #e9ece8;
    --title-red: #d8452a;
    --title-outline: #f1e2c8;
    --day-green: #9cc63a;
    --dish-gold: #d9c06a;
    --desc-yellow: #e6dd3c;
    --star-red: #b8322a;
  }

  html, body {
    margin: 0;
    padding: 0;
    width: 778px;
    height: 1200px;
    overflow: hidden;
    background: var(--board-dark);
  }

  .poster {
    position: relative;
    width: 778px;
    height: 1200px;
    background: var(--board-dark);
    overflow: hidden;
  }

  .chalkboard {
    position: absolute;
    inset: 22px;
    border-radius: 26px;
    background:
      radial-gradient(ellipse at 50% 35%, var(--board-light) 0%, var(--board-mid) 45%, #16191c 100%);
    box-shadow: inset 0 0 60px rgba(0,0,0,0.8);
  }

  .frame {
    position: absolute;
    inset: 0;
    width: 778px;
    height: 1200px;
  }

  .headline {
    position: absolute;
    left: 0;
    right: 0;
    text-align: center;
    margin: 0;
    font-family: "Rye", serif;
    font-weight: 400;
    line-height: 1;
  }

  .headline--special {
    top: 38px;
    font-size: 98px;
    color: var(--title-red);
    -webkit-text-stroke: 3px var(--title-outline);
    paint-order: stroke fill;
  }

  .headline--day {
    top: 178px;
    font-size: 74px;
    color: var(--day-green);
    -webkit-text-stroke: 2px #eef5d8;
    paint-order: stroke fill;
  }

  .headline--dish {
    top: 818px;
    font-size: 94px;
    color: var(--dish-gold);
    -webkit-text-stroke: 3px #f6efcf;
    paint-order: stroke fill;
  }

  .dish-description {
    position: absolute;
    top: 960px;
    left: 0;
    right: 0;
    margin: 0;
    text-align: center;
    font-family: "Bangers", sans-serif;
    font-size: 62px;
    line-height: 1.08;
    letter-spacing: 1px;
    color: var(--desc-yellow);
    -webkit-text-stroke: 1.5px #1a1a10;
  }

  .dish-illustration {
    position: absolute;
    left: 170px;
    top: 400px;
    width: 438px;
    height: 290px;
    border-radius: 50% / 45%;
    background: radial-gradient(ellipse at 50% 50%, #d6dadb 0%, #9ea4a7 55%, rgba(60,65,70,0) 100%);
    box-shadow: 0 0 0 6px rgba(43,143,184,0.55);
  }
</style>
</head>
<body>
  <main class="poster">
    <div class="chalkboard"></div>

    <svg class="frame" viewBox="0 0 778 1200" aria-hidden="true">
      <!-- board borders -->
      <rect x="22" y="22" width="734" height="1156" rx="26" fill="none" stroke="var(--frame-line)" stroke-width="4"/>
      <rect x="40" y="40" width="698" height="1120" rx="20" fill="none" stroke="var(--frame-blue)" stroke-width="3"/>

      <!-- corner bolts -->
      <g fill="none" stroke="var(--bolt-blue)" stroke-width="5">
        <circle cx="24" cy="24" r="16"/>
        <circle cx="754" cy="24" r="16"/>
        <circle cx="24" cy="1176" r="16"/>
        <circle cx="754" cy="1176" r="16"/>
      </g>

      <!-- star badges -->
      <g fill="var(--star-red)" stroke="#d9d9d9" stroke-width="3">
        <circle cx="88" cy="268" r="16"/>
        <circle cx="130" cy="268" r="16"/>
        <circle cx="648" cy="268" r="16"/>
        <circle cx="690" cy="268" r="16"/>
      </g>
      <g fill="#e8e8e8">
        <polygon points="88,257 91,265 99,265 92,270 95,278 88,273 81,278 84,270 77,265 85,265"/>
        <polygon points="130,257 133,265 141,265 134,270 137,278 130,273 123,278 126,270 119,265 127,265"/>
        <polygon points="648,257 651,265 659,265 652,270 655,278 648,273 641,278 644,270 637,265 645,265"/>
        <polygon points="690,257 693,265 701,265 694,270 697,278 690,273 683,278 686,270 679,265 687,265"/>
      </g>

      <!-- centre panel outline -->
      <rect x="124" y="300" width="530" height="490" rx="70" fill="none" stroke="var(--frame-blue)" stroke-width="5"/>

      <!-- side brackets -->
      <path d="M112 332 C 52 420, 52 625, 112 713 L 82 713 C 30 625, 30 420, 82 332 Z" fill="var(--chalk-white)" opacity="0.92"/>
      <path d="M666 332 C 726 420, 726 625, 666 713 L 696 713 C 748 625, 748 420, 696 332 Z" fill="var(--chalk-white)" opacity="0.92"/>
    </svg>

    <h1 class="headline headline--special">Daily Special</h1>
    <h2 class="headline headline--day">Friday</h2>

    <div class="dish-illustration" role="img" aria-label="Chalk-style illustration of a cod fish"></div>

    <h3 class="headline headline--dish">Fish N&#8217; Chips</h3>
    <p class="dish-description">Beer battered cod fish<br>and steak fries</p>
  </main>
</body>
</html>
```